Help our pizza bases / flat breads fly off the shelves - You'll be seen in supermarkets New Zealand

Packaging design.
We have bought a product that is in desperate need of a complete re-brand. This includes a name, and a package design.
It is an rectangle shaped flat bread that can be used in many ways, and is presented 5 in a pack, in an unprinted flexible formed bottom, with a flat top film applied that is flat and ready to receive your design.
The product is mainly used as a pizza base bought by Mums to feed the family. It is also can be a pre dinner nibble like a pizza bread, and for quick and easy, you can cut one into 3 pieces, and toast in a pop-up toaster, before topping with whatever is in your fridge.
The current name is "Kelmo breads" which is just silly. The brand "Kelmo" needs to change to "Dugald's Flat Breads" or whatever you might suggest. The product name might be "Tavira Pizza Base" or "Tavira Flat bread" as you like.
The look must get consumers to pick up the product and have a closer look. The nature of the graphics should emphasize the versatility and multi-usefulness, so the consumer can imagine what they will do with the product when they get it home. I feel that an informative pack will be better than a beautiful pack to get more sales. I have uploaded pictures showing the product currently in Supermarkets, and also a picture of the current product. Dimensions are 310 x 130mm.
You will need to leave room for: Barcode, Nutritional Panel, Cooking instructions, Storage instructions, Ingredients list and Company contact details - each one say 45 x 45mm or similar.
These details could go on the bottom of the low long side, as this is obscured while on shelf (see photo)
You will also highlight in your design, Preservative Free, 100% Natural, 5 Bases, Made with Olive oil, Hand made, and the variant (Roasted Garlic, or Original)
You will want to highlight the uses like: Pizza base, pizza bread, cut toast and top or similar.

```html
<!DOCTYPE html>
<html lang="en">
<head>
<meta charset="utf-8">
<title>Harlow Kitchen Tavira Pizza Base – Pack Range</title>
<link rel="stylesheet" href="https://fonts.googleapis.com/css2?family=Tinos:wght@400;700&display=swap">
<style>
  :root {
    --teal: #27b4c3;
    --ink: #141414;
    --garlic-red: #c8281f;
    --white: #ffffff;
    --tray-edge: #e4e6e8;
    --dough-light: #f1ebcf;
    --dough-mid: #e6dcb4;
    --uses-tone-a: #2d2d2d;
    --uses-tone-b: #6a7f82;
    --page: #ffffff;
  }
  * { margin: 0; padding: 0; box-sizing: border-box; }
  html, body {
    width: 1200px; height: 1114px; overflow: hidden;
    background: var(--page);
    font-family: "Tinos", "Times New Roman", serif;
  }
  .range { position: relative; width: 1200px; height: 1114px; }

  .pack {
    position: absolute; left: 120px; width: 966px; height: 442px;
    background: var(--white);
    border: 1px solid var(--tray-edge);
    border-radius: 14px;
    box-shadow: 0 10px 22px rgba(0,0,0,0.12);
    overflow: hidden;
  }
  .pack--original { top: 70px; }
  .pack--garlic { top: 572px; }

  .pack__product {
    position: absolute; left: 66px; top: 104px; width: 830px; height: 270px;
    border-radius: 10px;
    background: radial-gradient(ellipse at 50% 45%, var(--dough-light) 0%, var(--dough-mid) 100%);
  }
  .pack__band {
    position: absolute; left: 0; top: 6px; width: 100%; height: 150px;
    background: linear-gradient(to bottom, var(--teal) 0%, var(--teal) 68%, rgba(39,180,195,0) 100%);
  }

  .brand {
    position: absolute; left: 0; width: 100%; top: 52px;
    display: flex; justify-content: center; align-items: center; gap: 16px;
    font-weight: 700; font-size: 60px; line-height: 1;
    color: var(--white);
    letter-spacing: 2px;
  }
  .brand__dot {
    width: 20px; height: 20px; border-radius: 50%;
    background: var(--white);
  }
  .product-name {
    position: absolute; left: 0; width: 100%; top: 128px;
    text-align: center;
    font-weight: 700; font-size: 46px; line-height: 1;
    color: var(--teal);
    letter-spacing: 0.5px;
  }

  .count {
    position: absolute; left: 16px; top: 220px;
    writing-mode: vertical-rl;
    font-weight: 700; font-size: 19px; color: var(--ink);
    letter-spacing: 1px;
  }

  .uses-graphic {
    position: absolute; left: 52px; top: 196px; width: 104px; height: 160px;
    border-radius: 8px;
    background: linear-gradient(135deg, var(--uses-tone-a) 0%, var(--uses-tone-b) 100%);
    opacity: 0.85;
  }
  .uses-graphic--garlic {
    background: linear-gradient(135deg, var(--uses-tone-a) 0%, #8a4a44 100%);
  }

  .uses { list-style: none; position: absolute; left: 0; top: 0; }
  .uses li {
    position: absolute; white-space: nowrap;
    font-weight: 700; font-size: 14px; line-height: 18px; color: var(--ink);
  }
  .uses .use-base { left: 182px; top: 202px; }
  .uses .use-bread { left: 166px; top: 230px; }
  .uses .use-snack { left: 180px; top: 264px; }

  .variant {
    position: absolute; left: 0; width: 100%;
    text-align: center; font-weight: 700; line-height: 1;
  }
  .variant--original { top: 302px; font-size: 40px; color: var(--teal); }
  .variant--garlic { top: 316px; font-size: 25px; color: var(--garlic-red); }

  .claims {
    position: absolute; left: 0; width: 100%; top: 344px;
    text-align: center; font-size: 17px; color: var(--ink);
  }
</style>
</head>
<body>
<main class="range">

  <section class="pack pack--original" aria-label="Original pack">
    <div class="pack__product" role="img" aria-label="Photograph of the flat bread bases inside the tray"></div>
    <div class="pack__band"></div>
    <h1 class="brand"><span class="brand__dot" aria-hidden="true"></span>HARLOW KITCHEN</h1>
    <h2 class="product-name">TAVIRA PIZZA BASE</h2>
    <div class="count">5 BASES</div>

    <div class="uses-graphic" role="img" aria-label="Curved arrows graphic pointing to each way of using the base"></div>
    <ul class="uses">
      <li class="use-base">USE AS PIZZA BASE</li>
      <li class="use-bread">SERVE AS PIZZA BREAD</li>
      <li class="use-snack">CUT, TOAST AND TOP<br>FOR A SIMPLE SNACK</li>
    </ul>

    <p class="variant variant--original">ORIGINAL</p>
    <p class="claims">PRESERVATIVE FREE - 100% NATURAL, HAND MADE WITH OLIVE OIL</p>
  </section>

  <section class="pack pack--garlic" aria-label="Roasted garlic pack">
    <div class="pack__product" role="img" aria-label="Photograph of the flat bread bases inside the tray"></div>
    <div class="pack__band"></div>
    <h2 class="brand"><span class="brand__dot" aria-hidden="true"></span>HARLOW KITCHEN</h2>
    <h2 class="product-name">TAVIRA PIZZA BASE</h2>
    <div class="count">5 BASES</div>

    <div class="uses-graphic uses-graphic--garlic" role="img" aria-label="Curved arrows graphic pointing to each way of using the base"></div>
    <ul class="uses">
      <li class="use-base">USE AS PIZZA BASE</li>
      <li class="use-bread">SERVE AS PIZZA BREAD</li>
      <li class="use-snack">CUT, TOAST AND TOP<br>FOR A SIMPLE SNACK</li>
    </ul>

    <p class="variant variant--garlic">ROASTED GARLIC</p>
    <p class="claims">PRESERVATIVE FREE - 100% NATURAL, HAND MADE WITH OLIVE OIL</p>
  </section>

</main>
</body>
</html>
```